Web Design for Meadowfield Turf Crew

Meadowfield Turf Crew needs the photoshop files for a simple, clean and professional web design. I need a home and subpage design, although they can be very similar. See pagestridehub.com for a desired layout, although I'd like to see more design than shown on that site. The goal of the site is to attract both lawn maintenance/landscape customers and build a partner network of consultants that serve the US market. The following are needed:

- home and subpage design
- page: Home, Services, Locations, Consultants, FAQ, Contact
- if subpages have header photo, need to include 5 different header photos for each page
- favicon
Updates

I'll award the design based on the homepage concept. The minor subpage changes and other elements can be worked out in the workroom stage. Thanks, Trent

Industry/Entity Type

It Professional

```html
<!DOCTYPE html>
<html lang="en">
<head>
<meta charset="utf-8">
<title>Meadowfield Turf Crew — Home</title>
<link rel="stylesheet" href="https://fonts.googleapis.com/css2?family=Open+Sans:wght@400;600;700&family=Questrial&display=swap">
<style>
  :root {
    --green: #6ab43a;
    --green-dark: #4f9a2a;
    --ink: #3f4042;
    --grey: #6b6c6e;
    --grey-light: #a9aaab;
    --band: #f0f0f0;
    --footer: #5d5e60;
    --frame: #cfcfcf;
    --white: #ffffff;
    --link-blue: #2fa3de;
  }
  * { box-sizing: border-box; margin: 0; padding: 0; }
  html, body { width: 1200px; height: 1000px; overflow: hidden; background: var(--white); }
  body { position: relative; font-family: "Questrial", "Century Gothic", sans-serif; color: var(--ink); }
  .abs { position: absolute; }

  .page { position: absolute; left: 24px; top: 15px; width: 654px; height: 970px; border: 1px solid var(--frame); background: var(--white); overflow: hidden; }

  /* header */
  .brand { left: 73px; top: 17px; display: flex; align-items: center; gap: 7px; }
  .brand-dot { width: 12px; height: 12px; border-radius: 50%; background: var(--green); }
  .brand-name { font-size: 13px; color: var(--grey); letter-spacing: .3px; }
  .nav { left: 295px; top: 16px; display: flex; font-family: "Open Sans", sans-serif; font-size: 8.5px; color: var(--grey); }
  .nav a { text-decoration: none; color: inherit; padding: 5px 4px; margin-right: 4px; line-height: 11px; }
  .nav a.active { background: var(--green); color: var(--white); font-weight: 700; padding: 5px 7px; }

  /* hero */
  .hero { left: 0; top: 53px; width: 652px; height: 218px; background: linear-gradient(180deg, #1f7fd0 0%, #5fb1ec 45%, #8fbf5a 72%, #4f8f22 100%); }
  .hero-kicker { right: 72px; top: 17px; font-size: 13.5px; color: var(--white); letter-spacing: .2px; }
  .hero-title { right: 72px; top: 29px; font-family: "Questrial", sans-serif; font-size: 28px; font-weight: 700; color: #e8eef3; letter-spacing: -.3px; line-height: 30px; }
  .btn { display: block; background: var(--green); color: var(--white); font-family: "Open Sans", sans-serif; text-align: center; }
  .hero-btn { right: 72px; top: 57px; width: 68px; height: 21px; line-height: 21px; font-size: 9px; }
  .hero-shadow { left: 110px; top: 270px; width: 420px; height: 10px; border-radius: 50%; box-shadow: 0 4px 8px rgba(0,0,0,.18); }

  /* intro */
  .intro-title { left: 0; width: 652px; top: 288px; text-align: center; font-family: "Open Sans", sans-serif; font-weight: 700; font-size: 13.5px; line-height: 15px; color: var(--green); }
  .intro-title span { color: var(--ink); }
  .intro-text { left: 77px; width: 500px; top: 331px; text-align: center; font-size: 7.2px; line-height: 8.8px; color: var(--ink); }

  .card { top: 384px; width: 161px; }
  .card-img { width: 161px; height: 57px; }
  .card h3 { margin-top: 5px; font-family: "Open Sans", sans-serif; font-size: 7.2px; font-weight: 700; color: var(--ink); }
  .card p { margin-top: 6px; font-family: "Open Sans", sans-serif; font-size: 5.2px; line-height: 7px; color: var(--grey-light); }

  /* about + form band */
  .band { left: 0; top: 488px; width: 652px; height: 248px; background: var(--band); }
  .section-title { font-family: "Open Sans", sans-serif; font-weight: 700; font-size: 15px; color: var(--ink); }
  .section-title span { color: var(--green); }
  .about-title { left: 73px; top: 507px; }
  .about-text { left: 72px; width: 205px; top: 544px; font-size: 7.2px; line-height: 8.8px; color: var(--ink); }
  .about-text p + p { margin-top: 9px; }

  .form-photo { left: 286px; top: 500px; width: 291px; height: 224px; background: linear-gradient(180deg, #a9d3ec 0%, #cfe3ea 40%, #7fae58 68%, #3f7a2a 100%); }
  .form-panel { left: 328px; top: 500px; width: 210px; height: 224px; background: rgba(225,232,235,.78); border-radius: 0 0 6px 6px; }
  .form-title { left: 346px; top: 507px; }
  .field { position: absolute; left: 346px; width: 175px; height: 14px; background: var(--white); border: 1px solid #cfd3d5; font-size: 6.5px; color: #9a9c9e; padding: 2px 3px; line-height: 9px; }
  .field.message { height: 82px; }
  .submit { left: 454px; top: 698px; width: 67px; height: 20px; line-height: 20px; font-size: 8.5px; }

  /* locator */
  .locator { left: 73px; top: 748px; width: 412px; height: 100px; border: 1px solid #9fcf7f; border-radius: 6px; overflow: hidden; background: #fbfbf8; }
  .locator-map { left: 0; top: 0; width: 412px; height: 100px; background: linear-gradient(135deg, #efe3cf 0%, #f5ecdd 45%, #d8e6c9 70%, #eae0cf 100%); }
  .locator-fade { left: 200px; top: 0; width: 212px; height: 100px; background: linear-gradient(90deg, rgba(255,255,255,0) 0%, rgba(255,255,255,.92) 25%, rgba(255,255,255,.96) 100%); }
  .locator-title { left: 195px; width: 210px; top: 13px; text-align: center; font-size: 15px; }
  .locator-input { left: 216px; top: 33px; width: 188px; height: 25px; background: var(--white); border: 1px solid #dcdcdc; font-size: 12px; color: var(--grey); text-align: center; line-height: 23px; }
  .locator-btn { left: 255px; top: 63px; width: 111px; height: 24px; line-height: 24px; background: #6d6e70; color: var(--white); font-size: 9px; font-family: "Open Sans", sans-serif; text-align: center; }

  .contacts-title { left: 503px; top: 761px; font-size: 13px; }
  .contacts-address { right: 84px; top: 794px; text-align: right; font-family: "Open Sans", sans-serif; font-size: 5px; line-height: 7px; color: var(--grey); }
  .contacts-phones { right: 84px; top: 815px; width: 80px; text-align: right; font-family: "Open Sans", sans-serif; font-size: 5px; line-height: 7.5px; color: var(--grey); }
  .contacts-phones b { font-weight: 400; color: var(--link-blue); }
  .phone-dot { display: inline-block; width: 5px; height: 5px; border-radius: 50%; background: var(--link-blue); vertical-align: -1px; margin-right: 1px; }

  /* footer */
  .footer { left: 0; top: 860px; width: 652px; height: 88px; background: var(--footer); }
  .social { left: 279px; top: 889px; display: flex; gap: 2px; }
  .social span { width: 18px; height: 18px; background: #8a8b8d; }
  .footer-links { left: 0; width: 652px; top: 914px; text-align: center; font-family: "Open Sans", sans-serif; font-size: 7px; color: #e2e2e2; word-spacing: 1px; }
  .legal { left: 0; top: 948px; width: 652px; height: 22px; background: var(--green); color: var(--white); text-align: center; font-family: "Open Sans", sans-serif; font-size: 5.3px; line-height: 22px; }
  .legal u { font-weight: 700; }

  /* standalone lockup */
  .logo-lockup { left: 712px; top: 878px; display: flex; align-items: center; gap: 18px; height: 80px; }
  .logo-dot { width: 40px; height: 40px; border-radius: 50%; background: var(--green); }
  .logo-name { font-size: 34px; color: var(--grey); letter-spacing: .2px; white-space: nowrap; }
</style>
</head>
<body>
  <div class="page">
    <header>
      <div class="abs brand">
        <span class="brand-dot"></span>
        <span class="brand-name">Meadowfield Turf Crew</span>
      </div>
      <nav class="abs nav">
        <a class="active">HOME</a><a>SERVICES</a><a>LOCATIONS</a><a>CONSULTANTS</a><a>FAQ</a><a>CONTACT</a>
      </nav>
    </header>

    <section class="abs hero" role="img" aria-label="Photo of a lawn mower on a freshly cut lawn in front of houses under a blue sky">
      <div class="abs hero-kicker">LOREM IPSUM IS SIMPLY</div>
      <div class="abs hero-title">DUMMY TEXT</div>
      <a class="abs btn hero-btn">READ MORE</a>
    </section>
    <div class="abs hero-shadow"></div>

    <h1 class="abs intro-title">LOREM IPSUM IS SIMPLY DUMMY TEXT OF THE<br>PRINTING AND <span>TYPESETTING INDUSTRY.</span></h1>
    <p class="abs intro-text">Lorem Ipsum is simply dummy text of the printing and typesetting industry. Lorem Ipsum has been the industry's standard dummy text ever since the 1500s, when an unknown printer took a galley of type and scrambled it to make a type specimen book. It has survived not only five centuries, but also the leap into electronic typesetting, remaining essentially unchanged. It was popularised in the 1960s with the release of Transferline sheets containing Lorem Ipsum passages, and more recently with desktop publishing software like Folio LayoutDesk including versions of Lorem Ipsum.</p>

    <article class="abs card" style="left:73px">
      <div class="card-img" role="img" aria-label="Photo of an ornamental grass plant beside a lawn edge" style="background:linear-gradient(180deg,#8fc45a,#3f7d1f)"></div>
      <h3>Morbi nunc odio gravida atcursus nec</h3>
      <p>Aenean nonummy hendrerit mau phasellus nassetur ridic ulusm dui fusce feu. Cras...</p>
    </article>
    <article class="abs card" style="left:247px">
      <div class="card-img" role="img" aria-label="Photo of a red push mower on a sunny lawn" style="background:linear-gradient(180deg,#9ccf52,#5a9a24)"></div>
      <h3>Morbi nunc odio gravida atcursus nec</h3>
      <p>Aenean nonummy hendrerit mau phasellus nassetur ridic ulusm dui fusce feu. Cras...</p>
    </article>
    <article class="abs card" style="left:421px">
      <div class="card-img" role="img" aria-label="Photo of a riding mower on a park lawn with trees" style="background:linear-gradient(180deg,#b8d8e6 0%,#7aa85a 50%,#4d8a2a 100%)"></div>
      <h3>Morbi nunc odio gravida atcursus nec</h3>
      <p>Aenean nonummy hendrerit mau phasellus nassetur ridic ulusm dui fusce feu. Cras...</p>
    </article>

    <section class="abs band"></section>
    <h2 class="abs section-title about-title"><span>ABOUT</span> US</h2>
    <div class="abs about-text">
      <p>Lorem Ipsum is simply dummy text of the printing and typesetting industry. Lorem Ipsum has been the industry's standard dummy text ever since the 1500s, when an unknown printer took a galley of type and scrambled it to make a type specimen book. It has survived not only five centuries, but also the leap into electronic typesetting, remaining essentially unchanged. It was popularised in the 1960s with the release of Transferline sheets containing Lorem Ipsum passages, and more recently with desktop publishing software like Folio LayoutDesk including versions of Lorem Ipsum.</p>
      <p>Lorem Ipsum is simply dummy text of the printing and typesetting industry. Lorem Ipsum has been the industry's standard dummy text ever since the 1500s, when an unknown printer took a galley of type and scrambled it to make a type specimen book. It has survived not only five centuries, but also the leap into electronic typesetting, remaining essentially unchanged.</p>
    </div>

    <div class="abs form-photo" role="img" aria-label="Photo of a sunlit park lawn with trees and a pond"></div>
    <div class="abs form-panel"></div>
    <h2 class="abs section-title form-title"><span>GET</span> STARTED</h2>
    <div class="field" style="top:530px">First Name</div>
    <div class="field" style="top:551px">Last Name</div>
    <div class="field" style="top:572px">Email Address</div>
    <div class="field" style="top:593px">Phone Number</div>
    <div class="field message" style="top:614px">Type your message here</div>
    <a class="abs btn submit">SUBMIT</a>

    <section class="abs locator">
      <div class="abs locator-map" role="img" aria-label="Illustrated street map of a neighbourhood"></div>
      <div class="abs locator-fade"></div>
      <h2 class="abs section-title locator-title">FIND A LOCATION</h2>
      <div class="abs locator-input">City &amp; State or ZIP Code</div>
      <a class="abs locator-btn">FIND NOW!</a>
    </section>

    <h2 class="abs section-title contacts-title">CONTACTS</h2>
    <p class="abs contacts-address">4120 - 4126 Orchard Lane<br>Fairbrook, FB12 4QX</p>
    <p class="abs contacts-phones">Freephone: <span class="phone-dot"></span><b>+1 800 412 7730</b> Telephone: <span class="phone-dot"></span><b>+1 800 418 2264</b></p>

    <footer class="abs footer"></footer>
    <div class="abs social" aria-label="Social links">
      <span></span><span></span><span></span><span></span><span></span>
    </div>
    <div class="abs footer-links">SERVICES &nbsp;|&nbsp; LOCATIONS &nbsp;|&nbsp; CONSULTANTS &nbsp;|&nbsp; FAQ &nbsp;|&nbsp; CONTACT</div>
    <div class="abs legal">Copyright © 2014 Meadowfield Turf Crew. Use of this website constitutes acceptance of our <u>User Agreement</u> and <u>Privacy Policy</u></div>
  </div>

  <div class="abs logo-lockup">
    <span class="logo-dot"></span>
    <span class="logo-name">Meadowfield Turf Crew</span>
  </div>
</body>
</html>
```